Revamp PowerPoint deck to match our new website's visual identity and effectively tell our story

Revamp PowerPoint Deck to Match New Corporate Website Theme @ https://tivelquor7.hb-node.com/.
(Note: The content on the new theme is placeholder text. The current live website is www.pwlmetrix.com )

Key Request: Slide Master SHOULD NOT include any specific contents. It should contain only essential elements such master layout, the logo, header, footer, and any repeating text elements and it should be limited to a maximum of 5 pages.

We need to redesign our existing PowerPoint deck to align with the visual identity of our new corporate website while ensuring it effectively tells our story. The revamped deck should focus on:

1. Visual Storytelling: Each slide should guide the audience through a clear and compelling narrative. Build on each slide to ensure the story flows seamlessly.

2. Minimal Text, More Visuals: Avoid text-heavy slides. Where text is necessary, keep it concise. Focus on strong visuals, icons, and imagery that reinforce key points. Ensure the visuals are impactful and align with our brand identity. Use bold icons and high-quality images that match the tone of the new website to emphasize key messages.

3. Design Consistency: Ensure the presentation reflects the color palette, typography, and imagery from the new website. This includes maintaining consistency in the style of headings, subheadings, and body text to reinforce our brand identity.

4. Modern & Clean Design: Embrace a minimalist design aesthetic inspired by the new website. Use the same color schemes, fonts, and clean layouts to ensure the slides are visually engaging and easy to digest.

5. Professional, Minimalist Look: Keep the design professional and minimalist, with a focus on clarity. Ensure each slide conveys its message clearly without unnecessary distractions.

Our goal is to create a visually engaging and interactive presentation that clearly communicates our message while keeping the audience engaged.

Ensure our corporate color scheme is maintained as per the current website: www.pwlmetrix.com

Target Market(s)

B2B Clients in Asia Pacific and Australia

Industry/Entity Type

Across all industries, but more specific to IT

Requirements
Must have
• nsure our corporate color scheme is maintained as per the current website: www.pwlmetrix.com
Nice to have
• More graphics and illustrations than text. Icon representations.
Should not have
• Slide Master SHOULD NOT include any specific contents. It should contain only essential elements such master layout, the logo, header, footer, and any repeating text elements and it should be limited to a maximum of 5 pages

```html
<!DOCTYPE html>
<html lang="en">
<head>
<meta charset="utf-8">
<title>PWLMETRIX – Business Marketing Deck</title>
<link href="https://fonts.googleapis.com/css2?family=Montserrat:ital,wght@0,400;0,500;0,600;0,700;0,800;1,500&family=Open+Sans:wght@400;600&display=swap" rel="stylesheet">
<style>
:root{
  --navy:#263a63;
  --slate:#5a6a86;
  --red:#d42f2f;
  --ink:#2b2f3a;
  --grey:#6b6f78;
  --light:#eceef1;
  --board:#d9dbde;
  --white:#ffffff;
}
*{box-sizing:border-box;margin:0;padding:0}
html,body{width:1200px;height:1065px;overflow:hidden}
body{background:var(--board);font-family:"Montserrat",sans-serif;color:var(--ink);position:relative}
.slide{position:absolute;width:542px;height:305px;background:var(--white);overflow:hidden;box-shadow:0 3px 8px rgba(0,0,0,.18)}
.s1{left:47px;top:51px}.s2{left:610px;top:51px}
.s3{left:47px;top:380px}.s4{left:610px;top:380px}
.s5{left:47px;top:708px}.s6{left:610px;top:708px}
.abs{position:absolute}
.brand{position:absolute;font-weight:700;color:var(--red);letter-spacing:.08em;display:flex;align-items:center;gap:3px;line-height:1}
.brand .dot{width:4px;height:4px;background:var(--navy)}
.brand-sm{top:17px;right:12px;font-size:8.5px}
.photo{position:absolute}
.slide-title{position:absolute;left:19px;top:14px;font-size:17.5px;font-weight:700;color:var(--navy)}
.title-rule{position:absolute;left:19px;top:37px;width:36px;height:2.5px;background:var(--navy)}
.title-rule::after{content:"";position:absolute;left:38px;top:0;width:5px;height:2.5px;background:var(--red)}
.footer{position:absolute;left:22px;right:14px;bottom:14px;height:10px}
.footer .mark{position:absolute;left:0;bottom:0;width:6px;height:6px;background:var(--red)}
.footer .rule{position:absolute;left:12px;right:10px;bottom:1px;height:1px;background:var(--slate)}
.footer .copy{position:absolute;left:16px;bottom:3px;font-size:3.6px;color:#999}
.footer .num{position:absolute;right:0;bottom:-1px;font-size:5.5px;color:var(--navy)}
/* cover */
.cover-company{left:33px;top:112px;font-size:23px;font-weight:500;color:var(--slate)}
.cover-business{left:33px;top:136px;font-size:35px;font-weight:800;color:var(--red);line-height:1}
.cover-marketing{left:33px;top:176px;font-size:26px;font-weight:700;color:var(--navy);line-height:1}
.cover-pres{left:33px;top:217px;font-size:15px;font-style:italic;font-weight:500;color:var(--slate)}
.cover-lede{left:33px;top:237px;width:160px;font-size:7px;font-style:italic;line-height:1.35;color:var(--grey)}
.dots{left:33px;top:275px;display:flex;gap:6px}
.dots span{width:6px;height:6px;border-radius:50%;background:var(--navy)}
.dots span:nth-child(2){background:var(--red)}
/* agenda */
.agenda-word{left:86px;top:140px;font-size:29px;font-weight:700;color:var(--navy)}
.agenda-list{left:258px;top:74px;width:210px;list-style:none}
.agenda-list li{height:50px;position:relative;padding-left:14px}
.agenda-list li:nth-child(4){height:45px}
.agenda-list .n{position:absolute;left:0;top:0;font-size:12px;font-weight:700;color:var(--red)}
.agenda-list h3{font-size:12px;font-weight:600;color:var(--navy);line-height:1.2}
.agenda-list p{font-size:6.3px;color:var(--grey);line-height:1.3;margin-top:2px}
/* values */
.value{position:absolute;left:268px;width:250px}
.value .ring{position:absolute;left:0;top:0;width:42px;height:42px;border:2.5px solid var(--red);border-radius:50%;display:flex;align-items:center;justify-content:center}
.value h3{margin-left:58px;padding-top:7px;font-size:12.5px;font-weight:700;color:var(--navy)}
.value p{margin-left:58px;margin-top:3px;width:172px;font-size:6.8px;color:var(--grey);line-height:1.3}
/* cards */
.card{position:absolute;top:88px;width:87px;height:122px;border:1.8px solid var(--red);padding:26px 10px 0 11px;background:rgba(255,255,255,.6)}
.card.alt{border-color:var(--navy)}
.card .badge{position:absolute;left:50%;top:-14px;width:34px;height:34px;margin-left:-17px;border-radius:50%;background:var(--navy);display:flex;align-items:center;justify-content:center}
.card.alt .badge{background:var(--red)}
.card h3{font-size:8.8px;font-weight:700;color:var(--navy)}
.card p{font-size:4.6px;line-height:1.3;color:var(--grey);margin-top:3px}
.stat{left:80px;top:222px;font-size:16px;font-weight:700;color:var(--navy)}
.stat-copy{left:80px;top:247px;width:400px;font-size:6.2px;line-height:1.3;color:var(--grey)}
/* options */
.option{position:absolute;top:57px;width:102px}
.option .photo{position:relative;width:102px;height:120px}
.option .bar{height:4px;background:linear-gradient(90deg,var(--red),var(--navy))}
.option h3{margin-top:8px;font-size:10px;font-weight:500;color:var(--navy)}
.option h3 b{color:var(--red);font-weight:600}
.option p{margin-top:5px;width:76px;font-size:5.2px;line-height:1.35;color:var(--grey)}
/* thanks */
.brand-lg{left:269px;top:58px;font-size:22px}
.brand-lg .dot{width:8px;height:8px}
.thanks{left:268px;top:113px;font-size:35px;font-weight:800;color:var(--navy)}
.contact{position:absolute;left:268px;display:flex;align-items:center;font-family:"Open Sans",sans-serif;font-size:8.3px;color:var(--grey);line-height:1.25}
.contact svg{width:14px;height:14px;margin-right:6px}
.contact .sep{width:1px;height:16px;background:var(--grey);margin-right:8px}
.thanks-bar{left:181px;right:0;bottom:0;height:7px;background:linear-gradient(90deg,var(--red),var(--navy))}
.tile{position:absolute;background:var(--light)}
</style>
</head>
<body>

<!-- Cover -->
<section class="slide s1">
  <div class="brand" style="left:33px;top:44px;font-size:19px;">PWLMETRIX<span class="dot" style="width:7px;height:7px"></span></div>
  <div class="abs cover-company">Company</div>
  <div class="abs cover-business">Business</div>
  <div class="abs cover-marketing">Marketing</div>
  <div class="abs cover-pres">Presentation</div>
  <p class="abs cover-lede">Lorem ipsum dolor sit amet, consectetuer adipiscing elit, sed diam nonum</p>
  <div class="abs dots"><span></span><span></span><span></span></div>
  <svg class="abs" style="left:0;top:0" width="542" height="305" viewBox="0 0 924 520">
    <defs>
      <linearGradient id="coverFade" x1="0" y1="0" x2="1" y2="0">
        <stop offset="0" stop-color="#d42f2f"/><stop offset="1" stop-color="#263a63"/>
      </linearGradient>
      <linearGradient id="teamPhoto" x1="0" y1="0" x2="1" y2="1">
        <stop offset="0" stop-color="#b7a48e"/><stop offset=".55" stop-color="#e6e2dc"/><stop offset="1" stop-color="#4a4c52"/>
      </linearGradient>
    </defs>
    <polygon points="458,21 615,21 520,95" fill="#5a6a86"/>
    <polygon points="370,520 590,350 700,470 924,320 924,520" fill="url(#coverFade)"/>
    <polygon points="700,470 924,300 924,330 740,495" fill="#fff"/>
    <g role="img" aria-label="Photo of three colleagues reviewing a document at a desk">
      <polygon points="442,198 675,0 924,0 924,273 738,490" fill="url(#teamPhoto)"/>
    </g>
  </svg>
</section>

<!-- Agenda -->
<section class="slide s2">
  <div class="brand brand-sm">PWLMETRIX<span class="dot"></span></div>
  <svg class="abs" style="left:84px;top:130px" width="130" height="70" viewBox="0 0 130 70">
    <polygon points="0,3 46,3 0,19" fill="#263a63"/>
    <polygon points="54,48 130,48 88,66" fill="#d42f2f"/>
  </svg>
  <div class="abs agenda-word">Agenda</div>
  <ol class="abs agenda-list">
    <li><span class="n">1.</span><h3>Lorem ipsum</h3><p>Lorem ipsum dolor sit amet, consectetuer adipiscing elit, sed diam nonummy nibh euismod tincid</p></li>
    <li><span class="n">2.</span><h3>Lorem ipsum</h3><p>Lorem ipsum dolor sit amet, consectetuer adipiscing elit, sed diam nonummy nibh euismod tincid</p></li>
    <li><span class="n">3.</span><h3>Lorem ipsum</h3><p>Lorem ipsum dolor sit amet, consectetuer adipiscing elit, sed diam nonummy nibh euismod tincid</p></li>
    <li><span class="n">4.</span><h3>Lorem ipsum</h3><p>Lorem ipsum dolor sit amet, consectetuer adipiscing elit, sed diam nonummy nibh euismod tincid</p></li>
  </ol>
  <div class="footer"><span class="mark"></span><span class="rule"></span><span class="copy">Copyright @2023 PWLMetrix. All rights reserved.</span><span class="num">2</span></div>
</section>

<!-- Values -->
<section class="slide s3">
  <h2 class="slide-title">Text Added Hare</h2><span class="title-rule"></span>
  <div class="brand brand-sm">PWLMETRIX<span class="dot"></span></div>
  <div class="photo" role="img" aria-label="Black and white photo of a woman on a phone call" style="left:61px;top:69px;width:151px;height:182px;background:linear-gradient(135deg,#d8d8d8,#7a7a7a);border-right:3px solid var(--navy)"></div>
  <div class="photo" role="img" aria-label="Photo of a team meeting around a table with laptops" style="left:149px;top:90px;width:104px;height:139px;background:linear-gradient(160deg,#e9e4da,#b58a60 60%,#6b5a4a);border-top:3px solid var(--red)"></div>
  <div class="value" style="top:60px">
    <span class="ring"><svg width="22" height="18" viewBox="0 0 22 18" fill="#263a63"><circle cx="11" cy="5" r="3.5"/><circle cx="4.5" cy="7" r="2.5"/><circle cx="17.5" cy="7" r="2.5"/><path d="M5 17c0-4 2.7-7 6-7s6 3 6 7z"/><path d="M0 17c0-3 1.8-5 4.5-5 1 0 1.6.3 2 .6C5.2 14 4.6 15.5 4.5 17z"/><path d="M22 17c0-3-1.8-5-4.5-5-1 0-1.6.3-2 .6 1.3 1.4 1.9 2.9 2 4.4z"/></svg></span>
    <h3>We Before Me</h3>
    <p>ipsum dolor sit amet, cons ectetuer adipiscing elit, sed diam nonummy nibh euismod tincidunt ut laoreet</p>
  </div>
  <div class="value" style="top:136px">
    <span class="ring"><svg width="20" height="22" viewBox="0 0 20 22" fill="#263a63"><circle cx="6" cy="3" r="2.6"/><circle cx="14" cy="3" r="2.6"/><rect x="2.5" y="7" width="7" height="9" rx="2"/><rect x="10.5" y="7" width="7" height="9" rx="2"/><rect x="3.5" y="15" width="2.2" height="7"/><rect x="6.5" y="15" width="2.2" height="7"/><rect x="11.5" y="15" width="2.2" height="7"/><rect x="14.5" y="15" width="2.2" height="7"/></svg></span>
    <h3>We Are Good People</h3>
    <p>ipsum dolor sit amet, cons ectetuer adipiscing elit, sed diam nonummy nibh euismod tincidunt ut laoreet dolore magna aliquam erat volutpat.</p>
  </div>
  <div class="value" style="top:207px">
    <span class="ring"><svg width="24" height="20" viewBox="0 0 24 20" fill="#263a63"><path d="M12 11 7.5 6.8A2.7 2.7 0 0 1 12 3a2.7 2.7 0 0 1 4.5 3.8z"/><path d="M1 13h4l4 2h5a1.5 1.5 0 0 1 0 3H8v1l7 0 7-4a1.6 1.6 0 0 0-2-2.5L14 15v-1H9l-4-2H1z"/></svg></span>
    <h3>We Work with Heart</h3>
    <p>ipsum dolor sit amet, cons ectetuer adipiscing elit, sed diam nonummy nibh euismod tincidunt</p>
  </div>
  <div class="footer"><span class="mark"></span><span class="rule"></span><span class="copy">Copyright @2023 PWLMetrix. All rights reserved.</span><span class="num">3</span></div>
</section>

<!-- Services cards -->
<section class="slide s4">
  <h2 class="slide-title">Text Added Hare</h2><span class="title-rule"></span>
  <div class="brand brand-sm">PWLMETRIX<span class="dot"></span></div>
  <div class="abs" role="img" aria-label="Faint world map in the background" style="left:70px;top:50px;width:420px;height:180px;background:radial-gradient(ellipse at center,#eef0f2 0%,#f6f7f8 60%,rgba(255,255,255,0) 75%)"></div>
  <div class="card" style="left:79px">
    <span class="badge"><svg width="18" height="16" viewBox="0 0 18 16" fill="none" stroke="#fff" stroke-width="1.3"><rect x="3" y="1" width="14" height="9"/><path d="M6 8l3-3 2 2 4-4"/><circle cx="2.5" cy="12" r="1.5" fill="#fff"/><circle cx="8" cy="13" r="1.5" fill="#fff"/><circle cx="13" cy="13" r="1.5" fill="#fff"/></svg></span>
    <h3>Lorem ipsum</h3>
    <p>ipsum dolor sit amet, cons ectetuer adipiscing elit, sed diam nonummy nibh euismod tincidunt ut laoreet</p>
    <p>ipsum dolor sit amet, cons ectetuer adipiscing elit, sed diam nonummy nibh euismod tincidunt ut laoreet ipsum dolor sit amet, cons ectetuer</p>
  </div>
  <div class="card alt" style="left:181px">
    <span class="badge"><svg width="18" height="16" viewBox="0 0 18 16" fill="none" stroke="#fff" stroke-width="1.3"><rect x="1" y="1" width="14" height="10"/><path d="M4 9V6M7 9V4M10 9V7"/><circle cx="13" cy="11" r="2.5"/><path d="M15 13l2 2"/></svg></span>
    <h3>Lorem ipsum</h3>
    <p>ipsum dolor sit amet, cons ectetuer adipiscing elit, sed diam nonummy nibh euismod tincidunt ut laoreet</p>
    <p>ipsum dolor sit amet, cons ectetuer adipiscing elit, sed diam nonummy nibh euismod tincidunt ut laoreet ipsum dolor sit amet, cons ectetuer</p>
  </div>
  <div class="card" style="left:284px">
    <span class="badge"><svg width="18" height="14" viewBox="0 0 18 14" fill="#fff"><path d="M9 1 17 5 9 9 1 5z"/><path d="M4 7v3c0 1.5 2.3 2.5 5 2.5s5-1 5-2.5V7L9 9.5z"/><rect x="15.5" y="5" width="1" height="5"/></svg></span>
    <h3>Lorem ipsum</h3>
    <p>ipsum dolor sit amet, cons ectetuer adipiscing elit, sed diam nonummy nibh euismod tincidunt ut laoreet</p>
    <p>ipsum dolor sit amet, cons ectetuer adipiscing elit, sed diam nonummy nibh euismod tincidunt ut laoreet ipsum dolor sit amet, cons ectetuer</p>
  </div>
  <div class="card alt" style="left:387px">
    <span class="badge"><svg width="18" height="16" viewBox="0 0 18 16" fill="none" stroke="#fff" stroke-width="1.3"><rect x="1" y="4" width="16" height="10"/><circle cx="6" cy="8" r="1.8"/><path d="M3 13c0-2 1.3-3 3-3s3 1 3 3"/><rect x="10" y="1" width="6" height="4" fill="#fff"/></svg></span>
    <h3>Lorem ipsum</h3>
    <p>ipsum dolor sit amet, cons ectetuer adipiscing elit, sed diam nonummy nibh euismod tincidunt ut laoreet</p>
    <p>ipsum dolor sit amet, cons ectetuer adipiscing elit, sed diam nonummy nibh euismod tincidunt ut laoreet ipsum dolor sit amet, cons ectetuer</p>
  </div>
  <div class="abs stat">+ 35k</div>
  <p class="abs stat-copy">Lorem ipsum dolor sit amet, consectetuer adipiscing elit, sed diam nonummy nibh euismod tincidunt ut laoreet dolore magna aliquam erat volutpat. Ut wisi enim ad minim veniam, quis nostrud exerci tation ullamcorper</p>
  <div class="footer"><span class="mark"></span><span class="rule"></span><span class="copy">Copyright @2023 PWLMetrix. All rights reserved.</span><span class="num">4</span></div>
</section>

<!-- Options -->
<section class="slide s5">
  <h2 class="slide-title">Text Added Hare</h2><span class="title-rule"></span>
  <div class="brand brand-sm">PWLMETRIX<span class="dot"></span></div>
  <svg class="abs" style="left:33px;top:125px" width="61" height="65" viewBox="0 0 61 65"><polygon points="0,0 28,0 61,32 28,65 0,65 33,32" fill="#ededed"/></svg>
  <div class="option" style="left:128px">
    <div class="photo" role="img" aria-label="Photo of chess pieces on stacked wooden blocks" style="background:linear-gradient(180deg,#4a4a4a,#7a6a58 60%,#c89a6a)"></div>
    <div class="bar"></div>
    <h3>First <b>Option</b></h3>
    <p>Lorem ipsum dolor sit consectetuer adipiscing elit, sed diam nonummy nibh euismod tincidunt ut dolore magna aliquam erat volutpat. Ut wisi enim ad minim veniam, quis nostrud</p>
  </div>
  <div class="option" style="left:260px">
    <div class="photo" role="img" aria-label="Photo of a bright office with a jar on a desk" style="background:linear-gradient(135deg,#e8efe2,#f6f6f4 55%,#d9d4cf)"></div>
    <div class="bar"></div>
    <h3>Second <b>Option</b></h3>
    <p>Lorem ipsum dolor sit consectetuer adipiscing elit, sed diam nonummy nibh euismod tincidunt ut dolore magna aliquam erat volutpat. Ut wisi enim ad minim veniam, quis nostrud</p>
  </div>
  <div class="option" style="left:393px">
    <div class="photo" role="img" aria-label="Photo of a businessman raising a fist in celebration" style="background:linear-gradient(160deg,#f2f2f2,#9aa0a8 55%,#3a3e46)"></div>
    <div class="bar"></div>
    <h3>Third <b>Option</b></h3>
    <p>Lorem ipsum dolor sit consectetuer adipiscing elit, sed diam nonummy nibh euismod tincidunt ut dolore magna aliquam erat volutpat. Ut wisi enim ad minim veniam, quis nostrud</p>
  </div>
  <div class="footer"><span class="mark"></span><span class="rule"></span><span class="copy">Copyright @2023 PWLMetrix. All rights reserved.</span><span class="num">4</span></div>
</section>

<!-- Thank you -->
<section class="slide s6">
  <span class="tile" style="left:90px;top:46px;width:26px;height:26px"></span>
  <span class="tile" style="left:59px;top:97px;width:50px;height:50px"></span>
  <span class="tile" style="left:135px;top:87px;width:46px;height:46px"></span>
  <span class="tile" style="left:128px;top:154px;width:62px;height:62px"></span>
  <div class="brand brand-lg">PWLMETRIX<span class="dot"></span></div>
  <div class="abs thanks">Thank You</div>
  <div class="contact" style="top:168px">
    <svg viewBox="0 0 14 14"><path d="M3 1l2.5 3-1.5 1.5c.8 1.8 2.2 3.2 4 4L9.5 8l3 2.5-1.5 2.5C6 13 1 8 1 2.5z" fill="#d42f2f"/></svg>
    <span class="sep"></span><span>+61 2 5550 0147<br>+61 2 5550 0148</span>
  </div>
  <div class="contact" style="top:203px">
    <svg viewBox="0 0 14 14"><path d="M1 2l12 5-5 1.5L6.5 13z" fill="#d42f2f"/></svg>
    <span class="sep"></span><span>www.yourdomain.example<br>hello@yourdomain.example</span>
  </div>
  <div class="contact" style="top:234px">
    <svg viewBox="0 0 14 14"><path d="M7 1l6.5 5.5H12V13H8.5V9h-3v4H2V6.5H.5z" fill="#d42f2f"/></svg>
    <span class="sep"></span><span>45 Sample Road, Springvale,<br>NSW, Australia 2000.</span>
  </div>
  <div class="abs thanks-bar"></div>
</section>

</body>
</html>
```